Bold and colurful E-liquid Design Template

I'm looking for a new label for my house range of vape e-liquids. I currently have almost 40 flavours, so I'm looking for a single label design that I can modify to create the rest of the flavours.
Each label will have the same design, but I'll change the color for each flavour and the name.
I'd like the label to be predominantly text based with bold text and bold colours. I like bold typographic styles. Also for each flavour I'd like to add 1 - 3 letters to represent the flavour. This can be in a larger font.
eg for
Blueberry I'll use the letter B
Pineapple Peach will use PP
Cinnamon Blueberry Muffin uses TGS
The colour used on the label will also be important so they stand out nicely on the shelf.
I've attached a psd mockup of the bottles I'll be using.

```html
<!DOCTYPE html>
<html lang="en">
<head>
<meta charset="utf-8">
<title>Premium E-Liquids Label Range</title>
<link rel="stylesheet" href="https://fonts.googleapis.com/css2?family=Orbitron:wght@700;900&display=swap">
<style>
  :root {
    --backdrop: #a7a8ab;
    --label-white: #ffffff;
    --blueberry: #1ea1dc;
    --peach-pineapple: #f2a535;
    --berry-plum: #9b1c5b;
  }
  * { margin: 0; padding: 0; box-sizing: border-box; }
  html, body {
    width: 1084px;
    height: 1200px;
    overflow: hidden;
    background: var(--backdrop);
    font-family: "Orbitron", sans-serif;
  }
  .range {
    display: flex;
    gap: 46px;
    padding: 180px 46px 0;
  }
  .label {
    position: relative;
    width: 300px;
    height: 840px;
    background: var(--label-white);
    color: var(--accent);
    overflow: hidden;
  }
  .label--blueberry { --accent: var(--blueberry); }
  .label--peach { --accent: var(--peach-pineapple); }
  .label--plum { --accent: var(--berry-plum); }
  .label__band {
    position: absolute;
    top: 0;
    left: 0;
    width: 300px;
    height: 150px;
    fill: var(--accent);
  }
  .label__text {
    position: absolute;
    left: 50%;
    bottom: 150px;
    height: 600px;
    writing-mode: vertical-rl;
    transform: translateX(-50%) rotate(180deg);
    text-transform: uppercase;
    white-space: nowrap;
  }
  .label__tagline {
    font-weight: 700;
    font-size: 25px;
    line-height: 36px;
    letter-spacing: 0.5px;
  }
  .label__flavour {
    font-weight: 900;
    font-size: 60px;
    line-height: 64px;
  }
  .label__code {
    font-weight: 900;
    font-size: 112px;
    line-height: 112px;
  }
  .label__spec {
    position: absolute;
    left: 25px;
    right: 25px;
    bottom: 62px;
    height: 72px;
    background: var(--accent);
    color: var(--label-white);
    font-weight: 900;
    font-size: 27px;
    display: flex;
    align-items: center;
    justify-content: center;
    gap: 16px;
  }
  .label__divider {
    width: 3px;
    height: 32px;
    background: var(--label-white);
  }
</style>
</head>
<body>
  <main class="range">
    <article class="label label--blueberry">
      <svg class="label__band" viewBox="0 0 300 150" aria-hidden="true">
        <path d="M0 0 H300 V72 C210 72 110 105 0 135 Z"/>
      </svg>
      <div class="label__text">
        <p class="label__tagline">Premium E-Liquids</p>
        <p class="label__flavour">Blueberry</p>
      </div>
      <div class="label__spec"><span>3MG</span><span class="label__divider"></span><span>100ML</span></div>
    </article>

    <article class="label label--peach">
      <svg class="label__band" viewBox="0 0 300 150" aria-hidden="true">
        <path d="M0 0 H300 V72 C210 72 110 105 0 135 Z"/>
      </svg>
      <div class="label__text">
        <p class="label__flavour">Peach</p>
        <p class="label__flavour">Pineapple</p>
        <p class="label__tagline">Premium E-Liquids</p>
      </div>
      <div class="label__spec"><span>3MG</span><span class="label__divider"></span><span>100ML</span></div>
    </article>

    <article class="label label--plum">
      <svg class="label__band" viewBox="0 0 300 150" aria-hidden="true">
        <path d="M0 0 H300 V72 C210 72 110 105 0 135 Z"/>
      </svg>
      <div class="label__text">
        <p class="label__code">TGS</p>
        <p class="label__tagline">Premium E-Liquids</p>
      </div>
      <div class="label__spec"><span>3MG</span><span class="label__divider"></span><span>100ML</span></div>
    </article>
  </main>
</body>
</html>
```